8"x5" postcard for Wireless Internet introduction to new mountain town market

I need to market high speed internet to a resort mountain town without doing the obvious laptop on a mountain top thing, so tired. We are going to be competing directly with another provider with same cost, but we will be offering free installation. The area is Aspen Colorado, so the clientele are outdoor types who have suffered for years from being disconnected in their mountain town. We offer fast internet and excellent customer service from people who live in their neck of the woods.

Target Market(s)

23-55 years old, both resort living, families and ski bums

Font styles to use
Sans Serif

Colors

Designer to choose colors to be used in the design.

Requirements
Must have
• Visual appeal and fresh verbiage. We don't mind being a little edgy. We are a young company and we want to appeal to people looking for a provider who gets them. We prefer a clean look.
Nice to have
• Nice to have colors that match our logo
Should not have
• stuffy concepts or verbiage that is too much like a car salesman. We don't want to look like a 'big box' company.

```html
<!DOCTYPE html>
<html lang="en">
<head>
<meta charset="utf-8">
<title>Ridgeway Broadband – High Speed Internet Postcard</title>
<link rel="stylesheet" href="https://fonts.googleapis.com/css2?family=Open+Sans:wght@400;700;800&family=Catamaran:wght@400;500&display=swap">
<style>
  :root {
    --backdrop: #ececec;
    --ink: #231f20;
    --charcoal: #333336;
    --amber: #f7a823;
    --orange: #f39a1e;
    --yellow: #fcd116;
    --white: #ffffff;
    --sky: #aebfcc;
    --haze: #d9c7b4;
    --forest: #2f3427;
  }
  html, body {
    margin: 0;
    width: 1200px;
    height: 1200px;
    overflow: hidden;
    background: var(--backdrop);
  }
  .postcard {
    position: absolute;
    left: 250px;
    top: 40px;
    width: 700px;
    height: 1120px;
    filter: drop-shadow(6px 8px 14px rgba(0,0,0,.35));
  }
  .brand-name { font-family: "Open Sans", sans-serif; font-weight: 700; font-size: 38px; fill: var(--charcoal); }
  .headline {
    font-family: "Open Sans", sans-serif; font-weight: 800; font-size: 74px;
    fill: var(--ink); stroke: var(--white); stroke-width: 3px; paint-order: stroke;
    letter-spacing: -1px;
  }
  .tagline { font-family: "Open Sans", sans-serif; font-weight: 700; font-size: 35px; fill: var(--white); }
  .feature { font-family: "Catamaran", sans-serif; font-weight: 400; font-size: 31px; fill: var(--ink); }
  .price { font-family: "Catamaran", sans-serif; font-weight: 500; font-size: 56px; fill: var(--ink); }
  .call-now { font-family: "Open Sans", sans-serif; font-weight: 700; font-size: 37px; fill: var(--white); }
  .contact { font-family: "Catamaran", sans-serif; font-weight: 400; font-size: 29px; fill: var(--ink); }
</style>
</head>
<body>
<svg class="postcard" viewBox="0 0 842 1348" xmlns="http://www.w3.org/2000/svg">
  <defs>
    <linearGradient id="photo-tones" x1="0" y1="0" x2="0" y2="1">
      <stop offset="0" stop-color="var(--sky)"/>
      <stop offset="0.33" stop-color="var(--haze)"/>
      <stop offset="0.5" stop-color="#7b776a"/>
      <stop offset="0.72" stop-color="var(--forest)"/>
      <stop offset="1" stop-color="#3c362c"/>
    </linearGradient>
    <linearGradient id="offer-glow" x1="0" y1="0" x2="1" y2="1">
      <stop offset="0" stop-color="var(--orange)"/>
      <stop offset="0.6" stop-color="#e48a22"/>
      <stop offset="1" stop-color="#8a5a1c"/>
    </linearGradient>
    <linearGradient id="contact-glow" x1="0" y1="1" x2="1" y2="0">
      <stop offset="0" stop-color="var(--yellow)"/>
      <stop offset="1" stop-color="var(--amber)"/>
    </linearGradient>
    <clipPath id="photo-clip">
      <polygon points="0,0 400,0 842,135 842,780 0,545"/>
    </clipPath>
  </defs>

  <rect class="card-base" width="842" height="1348" fill="var(--ink)"/>

  <polygon points="400,0 842,0 842,135" fill="var(--amber)"/>
  <rect x="775" y="0" width="67" height="50" fill="var(--ink)"/>
  <polygon points="775,50 842,50 842,68" fill="var(--ink)"/>

  <g role="img" aria-label="Photo of a young man leaping over a rocky mountain ledge above forested valleys at sunset">
    <polygon points="0,0 400,0 842,135 842,780 0,545" fill="url(#photo-tones)"/>
    <rect x="432" y="0" width="410" height="780" fill="#3a3d42" opacity="0.35" clip-path="url(#photo-clip)"/>
  </g>
  <polygon class="divider" points="400,0 418,0 842,128 842,140" fill="var(--white)"/>

  <polygon points="68,560 842,775 842,800 68,1303" fill="url(#offer-glow)"/>
  <polygon points="0,1290 68,1245 68,1303 0,1348" fill="var(--yellow)"/>
  <polygon class="divider" points="0,540 842,775 842,795 0,560" fill="var(--white)"/>

  <polygon points="842,812 842,1348 28,1348" fill="url(#contact-glow)"/>
  <polygon class="divider" points="842,790 842,812 28,1348 0,1348 0,1335" fill="var(--white)"/>
  <polygon points="775,935 842,890 842,1348 775,1348" fill="var(--ink)"/>

  <text class="brand-name" x="40" y="95">Ridgeway Broadband</text>

  <text class="headline" text-anchor="end" x="805" y="213">HIGH</text>
  <text class="headline" text-anchor="end" x="805" y="287">SPEED</text>
  <text class="headline" text-anchor="end" x="805" y="362">INTERNET</text>
  <rect x="477" y="386" width="328" height="7" fill="var(--ink)"/>
  <rect x="477" y="396" width="328" height="7" fill="var(--amber)"/>

  <text class="tagline" x="99" y="695">Better,</text>
  <text class="tagline" x="99" y="740">Not Bigger!</text>
  <text class="feature" x="99" y="828">Free residential Installation</text>
  <text class="feature" x="99" y="873">In-House Tech Support</text>
  <text class="feature" x="99" y="918">10, 25 and 40Mbps</text>
  <circle cx="677" cy="818" r="35" fill="var(--ink)"/>
  <text class="feature" x="99" y="1005">Prices start at</text>
  <text class="price" x="97" y="1070">$59.95</text>

  <text class="call-now" text-anchor="end" x="743" y="1072">Call Now</text>
  <text class="contact" text-anchor="end" x="743" y="1160">1 800 555 0142</text>
  <text class="contact" text-anchor="end" x="743" y="1205">1 720 555 0178</text>
  <text class="contact" text-anchor="end" x="743" y="1250">www.ridgewaynet.com/connect</text>
  <text class="contact" text-anchor="end" x="743" y="1295">hello@ridgewaybroadband.com</text>
</svg>
</body>
</html>
```